Need Power Point Presentation - That incorporates New Logo

We have a new logo and would like to incorporate it into a Power Point template. We are looking for title page, 2 body pages and a closing page design. If you have any questions please let me know. New logo is attached.

```html
<!DOCTYPE html>
<html lang="en">
<head>
<meta charset="UTF-8">
<title>The Presentation Title</title>
<link rel="stylesheet" href="https://fonts.googleapis.com/css2?family=Montserrat:wght@400&family=Source+Sans+3:wght@400;600;700&display=swap">
<style>
  :root {
    --navy: #0a4778;
    --deep-blue: #0d6fa3;
    --sky: #55cff7;
    --pale-sky: #e8f8ff;
    --band-blue: #1c9ec9;
    --title-blue: #164b82;
    --subtitle-grey: #6d6e70;
    --haze-grey: #eef1f4;
    --go-green: #2cb52c;
    --white: #ffffff;
  }
  html, body {
    margin: 0;
    padding: 0;
    width: 1200px;
    height: 900px;
    overflow: hidden;
    background: var(--white);
  }
  .slide {
    position: relative;
    width: 1200px;
    height: 900px;
    overflow: hidden;
    background: var(--white);
    font-family: "Source Sans 3", Arial, sans-serif;
  }
  .wave-backdrop {
    position: absolute;
    inset: 0;
  }
  .brand {
    position: absolute;
    left: 68px;
    top: 150px;
    display: flex;
    align-items: center;
    gap: 22px;
  }
  .brand-dot {
    width: 34px;
    height: 34px;
    border-radius: 50%;
    background: var(--white);
  }
  .brand-name {
    color: var(--white);
    font-family: "Source Sans 3", Arial, sans-serif;
    font-weight: 400;
    font-size: 78px;
    letter-spacing: 4px;
    line-height: 1;
  }
  .title {
    position: absolute;
    left: 61px;
    top: 585px;
    margin: 0;
    color: var(--title-blue);
    font-weight: 600;
    font-size: 56px;
    line-height: 1;
    white-space: nowrap;
  }
  .subtitle {
    position: absolute;
    left: 62px;
    top: 648px;
    margin: 0;
    color: var(--subtitle-grey);
    font-family: "Montserrat", Arial, sans-serif;
    font-size: 23px;
    line-height: 1.2;
    letter-spacing: 0.3px;
    white-space: nowrap;
  }
  .start-frame {
    position: absolute;
    left: 65px;
    top: 722px;
    width: 196px;
    height: 72px;
    border: 1px solid var(--go-green);
    box-sizing: border-box;
  }
  .start-button {
    position: absolute;
    left: 9px;
    top: 9px;
    width: 176px;
    height: 52px;
    background: var(--go-green);
    color: var(--white);
    font-weight: 700;
    font-size: 37px;
    line-height: 52px;
    text-decoration: none;
    letter-spacing: 0.3px;
    display: flex;
    align-items: center;
    justify-content: center;
    gap: 10px;
  }
  .start-chevron {
    width: 12px;
    height: 22px;
  }
</style>
</head>
<body>
<main class="slide">
  <svg class="wave-backdrop" width="1200" height="900" viewBox="0 0 1200 900" aria-hidden="true">
    <defs>
      <linearGradient id="sky-fill" x1="0" y1="0" x2="1" y2="0.2">
        <stop offset="0" stop-color="var(--navy)"/>
        <stop offset="0.3" stop-color="var(--deep-blue)"/>
        <stop offset="0.55" stop-color="var(--sky)"/>
        <stop offset="1" stop-color="#9fe4fb"/>
      </linearGradient>
      <radialGradient id="sky-glow" cx="1060" cy="260" r="260" gradientUnits="userSpaceOnUse">
        <stop offset="0" stop-color="var(--pale-sky)" stop-opacity="1"/>
        <stop offset="1" stop-color="var(--pale-sky)" stop-opacity="0"/>
      </radialGradient>
      <linearGradient id="band-fill" x1="0" y1="0" x2="1" y2="0">
        <stop offset="0" stop-color="var(--white)"/>
        <stop offset="0.35" stop-color="#6cc4de"/>
        <stop offset="0.7" stop-color="var(--band-blue)"/>
        <stop offset="1" stop-color="#2aa6d0"/>
      </linearGradient>
      <linearGradient id="haze-fill" x1="0" y1="0" x2="0" y2="1">
        <stop offset="0" stop-color="var(--haze-grey)" stop-opacity="0.9"/>
        <stop offset="1" stop-color="var(--haze-grey)" stop-opacity="0"/>
      </linearGradient>
    </defs>

    <path class="sky-panel" fill="url(#sky-fill)"
      d="M0,0 H1200 V380 C1150,470 1060,500 960,470 C860,445 800,430 760,420 C620,370 380,340 0,372 Z"/>
    <path class="sky-glow" fill="url(#sky-glow)"
      d="M0,0 H1200 V380 C1150,470 1060,500 960,470 C860,445 800,430 760,420 C620,370 380,340 0,372 Z"/>

    <path class="light-band" fill="url(#band-fill)"
      d="M0,372 C380,340 620,370 760,420 C860,455 1000,500 1100,470 C1150,455 1180,430 1200,410
         V455 C1120,520 1000,540 880,525 C800,512 760,500 720,482 C560,420 320,400 0,455 Z"/>
  </svg>

  <svg class="wave-haze" role="img" aria-label="Soft decorative line pattern below the wave"
       width="1200" height="900" viewBox="0 0 1200 900" style="position:absolute;inset:0;">
    <path fill="url(#haze-fill)"
      d="M770,500 C840,600 890,682 940,682 C1000,682 1050,600 1110,505 C1040,530 960,532 880,522 C830,515 800,508 770,500 Z"/>
  </svg>

  <div class="brand">
    <span class="brand-dot"></span>
    <span class="brand-name">MERIDANE</span>
  </div>

  <h1 class="title">The Presentation Title</h1>
  <p class="subtitle">John Doe, 1 January 2014</p>

  <div class="start-frame">
    <a class="start-button" href="#">START
      <svg class="start-chevron" viewBox="0 0 12 22" aria-hidden="true">
        <path d="M2,2 L10,11 L2,20" fill="none" stroke="var(--white)" stroke-width="2.4"/>
      </svg>
    </a>
  </div>
</main>
</body>
</html>
```